" Empresa jovem, em franca expansao, com necessidade de ampliar e qualificar sua carteira de clientes, buscando aprimorar sua identidade visual para se destacar em uma concorrência com pouco investimento nesse fundamento corporativo e potencializar sua apresentaçao a clientes de grande porte. "

```html
<!DOCTYPE html>
<html lang="pt-BR">
<head>
<meta charset="UTF-8">
<title>Afiadora Montalvo — Envelopes</title>
<link rel="stylesheet" href="https://fonts.googleapis.com/css2?family=Michroma&family=Open+Sans:wght@400;600&display=swap">
<style>
  :root {
    --bg: #ecebe8;
    --paper: #ffffff;
    --navy: #0e2d4f;
    --green: #11a04f;
    --green-dark: #0c8a42;
    --grey-text: #c8ccd2;
  }
  * { margin: 0; padding: 0; box-sizing: border-box; }
  html, body { width: 1200px; height: 1200px; overflow: hidden; background: var(--bg); }
  .canvas { position: relative; width: 1200px; height: 1200px; }

  .envelope { position: absolute; box-shadow: 0 14px 30px rgba(0,0,0,0.22); }

  .envelope--front {
    left: 110px; top: 190px; width: 500px; height: 790px;
    background: var(--paper);
  }
  .envelope--front .flap-band {
    position: absolute; left: 0; top: 0; width: 100%; height: 72px; background: var(--green);
  }
  .brand {
    position: absolute; right: 32px; bottom: 150px;
    display: flex; align-items: flex-end; gap: 14px;
  }
  .brand__mark { width: 34px; height: 34px; background: var(--navy); margin-bottom: 6px; }
  .brand__text { display: flex; flex-direction: column; align-items: flex-start; }
  .brand__kicker {
    font-family: "Michroma", sans-serif; font-size: 11px; letter-spacing: 9px;
    color: var(--navy); margin-left: 4px; margin-bottom: 4px;
  }
  .brand__name {
    font-family: "Michroma", sans-serif; font-size: 30px; letter-spacing: 1px;
    color: var(--navy); line-height: 1;
  }

  .envelope--back {
    left: 625px; top: 300px; width: 480px; height: 780px;
    background: var(--navy);
  }
  .envelope--back svg { position: absolute; left: 0; top: 0; }
  .back-info {
    position: absolute; left: 0; right: 0; bottom: 90px; text-align: center;
    font-family: "Open Sans", sans-serif; color: var(--grey-text);
  }
  .back-info__mark { width: 14px; height: 14px; background: var(--grey-text); margin: 0 auto 6px; }
  .back-info__name { font-family: "Michroma", sans-serif; font-size: 10px; letter-spacing: 1px; margin-bottom: 14px; color: #ffffff; }
  .back-info__address { font-size: 9px; margin-bottom: 10px; }
  .back-info__web { font-size: 9px; }
</style>
</head>
<body>
<main class="canvas">
  <section class="envelope envelope--front">
    <div class="flap-band"></div>
    <div class="brand">
      <div class="brand__mark"></div>
      <div class="brand__text">
        <span class="brand__kicker">AFIADORA</span>
        <span class="brand__name">MONTALVO</span>
      </div>
    </div>
  </section>

  <section class="envelope envelope--back">
    <svg width="480" height="780" viewBox="0 0 480 780">
      <polygon points="0,0 480,0 480,72 455,98 25,98 0,72" fill="var(--green)"/>
      <line x1="25" y1="98" x2="455" y2="98" stroke="var(--green-dark)" stroke-width="2"/>
      <polygon points="0,740 14,734 466,734 480,740 480,780 0,780" fill="var(--green)"/>
    </svg>
    <div class="back-info">
      <div class="back-info__mark"></div>
      <div class="back-info__name">MONTALVO</div>
      <p class="back-info__address">Av. Serrana, 410 Jardim Alto - Montalvo - MG - 32 4100-0000</p>
      <p class="back-info__web">www.montalvo.com.br</p>
    </div>
  </section>
</main>
</body>
</html>
```